Review Site Redesign

We have a rather ambitious goal to reinvent (redesign) the way bank financial review sites present information. In that respect, we’re looking for an innovative creative design.
As examples of what I would call bad or boring design please look at the following sites:
1. http://brisklend.example/se
2. http://vantorquay.example/se/privatlan
3. http://glimsworth.example/no
These are the traditional way these types of review sites are organized: dull and boring. I think we can do a lot better than that.
I need a site that will capture attention end engage the visitor; a site that will create a more interactive and less passive user experience.
Scope of work should also include logo font and additional content space for articles, FAQ, widgets, social media links, etc.

Not sure what to advise you as best format - maybe a flash or js carousel, gallery, wheel, logo image matrix, or something else.
Maybe some kind of interactive logo matrix such as this site: http://www.quarnibo.example/
Please apply your best creative mind work to this problem.
Also, please think about creative use of background images, stock photos, etc.
For logo font use can use URL “pellrowatt.example” as placeholder.

```html
<!DOCTYPE html>
<html lang="en">
<head>
<meta charset="utf-8">
<title>pellrowatt.example — Loan Reviews</title>
<link href="https://fonts.googleapis.com/css2?family=Roboto:wght@400;500;700&display=swap" rel="stylesheet">
<style>
:root{
  --red:#e0301e;
  --red-dark:#b8210f;
  --green:#3aa524;
  --dark:#2e2e2e;
  --dark-2:#3c3c3c;
  --page:#ebebeb;
  --text:#444;
  --muted:#888;
  --line:#dcdcdc;
  --star:#f4a800;
  --white:#fff;
}
*{box-sizing:border-box;margin:0;padding:0}
html,body{width:957px;height:1200px;overflow:hidden}
body{background:linear-gradient(90deg,#e6e6e6,#f0f0f0 50%,#e6e6e6);font-family:"Roboto",Arial,sans-serif;color:var(--text);position:relative;font-size:9px}
ul{list-style:none}
.abs{position:absolute}

/* header */
.brand{left:143px;top:28px;font-size:25px;color:#4a4a4a;font-weight:500;letter-spacing:-.3px}
.hotline{left:432px;top:27px;display:flex;align-items:center;gap:10px}
.phone-badge{width:22px;height:22px;border-radius:50%;border:2px solid var(--red);display:flex;align-items:center;justify-content:center}
.hotline small{display:block;color:var(--red);font-size:9px}
.hotline strong{font-size:15px;color:#222;font-weight:700;letter-spacing:.3px}
.search{left:666px;top:28px;width:146px;height:22px;background:var(--white);border:1px solid #d6d6d6;border-radius:2px;display:flex;align-items:center;justify-content:space-between;padding:0 8px;color:#999;font-size:9px}

/* nav */
.mainnav{left:126px;top:78px;width:705px;height:29px;background:linear-gradient(#ec3b24,#cc2612);display:flex;align-items:center;padding-left:6px;border-radius:3px 3px 0 0}
.mainnav a{color:var(--white);text-decoration:none;font-size:12px;font-weight:500;padding:0 12px;height:29px;line-height:29px;position:relative}
.mainnav a+a::before{content:"";position:absolute;left:0;top:9px;width:4px;height:4px;background:rgba(255,255,255,.6);transform:rotate(45deg)}
.mainnav a.active{background:#b61e0d}
.subnav{left:126px;top:107px;width:705px;height:21px;background:#333;display:flex;align-items:center;padding-left:16px;gap:20px;color:#bbb;font-size:9px}
.subnav .connect{margin-left:auto;display:flex;align-items:center;gap:6px;padding-right:12px;color:#ddd;font-style:italic}
.subnav .dot{width:8px;height:8px;background:#ddd;border-radius:2px}

/* hero */
.hero{left:126px;top:142px;width:507px;height:249px;background:linear-gradient(120deg,#d9dee3 0%,#f3f3f1 35%,#c9cfd6 60%,#7d8a99 100%)}
.hero .dots{position:absolute;left:12px;bottom:12px;display:flex;gap:5px}
.hero .dots i{width:8px;height:8px;border-radius:50%;background:var(--white)}
.hero .dots i:first-child{background:#444;border:2px solid #fff}

/* panels */
.panel{background:var(--white);box-shadow:0 1px 2px rgba(0,0,0,.15)}
.panel-head{height:27px;background:linear-gradient(#464646,#2f2f2f);border-bottom:3px solid var(--red);color:var(--white);font-size:10.5px;display:flex;align-items:center;gap:8px;padding-left:12px}
.panel-head svg{flex:none}

.chooser{left:645px;top:142px;width:186px;height:252px}
.chooser section{padding:8px 12px 6px;border-bottom:1px solid #eee}
.chooser h4{font-size:10px;font-weight:500;color:#333;margin-bottom:3px}
.chooser li{font-size:8px;color:#666;line-height:12.5px;padding-left:11px;position:relative}
.chooser li::before{content:"";position:absolute;left:1px;top:4px;width:4px;height:4px;border:1px solid #888;border-radius:50%}
.chooser p{font-size:8px;color:#555}
.vote{display:flex;align-items:center;gap:10px;margin-top:8px;font-size:8px;color:#666}
.vote i{display:inline-block;width:8px;height:8px;border-radius:50%;border:1px solid #aaa;vertical-align:-1px;margin-right:3px}
.vote .btn{margin-left:auto}
.btn{background:var(--red);color:var(--white);font-size:8.5px;font-weight:700;padding:3px 10px;border-radius:2px}

/* table */
.lending{left:126px;top:410px;width:507px;height:543px}
.lending .panel-head{background:var(--red);border:0;border-radius:3px 3px 0 0;height:27px}
.cols{display:grid;grid-template-columns:86px 97px 74px 112px 138px}
.thead{height:32px;background:#444;color:#ddd;font-size:9.5px}
.thead div{display:flex;align-items:center;padding-left:12px;border-right:1px solid #555}
.thead div:nth-child(n+2){justify-content:center;padding:0}
.row{height:81px;border-bottom:1px solid var(--line);position:relative}
.row:nth-child(even){background:#fafafa}
.row .cols{height:56px;align-items:center}
.supplier{text-align:center}
.logo-box{width:68px;height:33px;margin:8px auto 0;border:1px solid #ddd;background:var(--white);display:flex;align-items:center;justify-content:center;font-size:9px;font-weight:700;color:#333;gap:4px}
.logo-box b{width:7px;height:7px;background:var(--red);border-radius:50%}
.supplier-name{position:absolute;left:0;top:60px;width:86px;text-align:center;color:var(--red);font-size:8.5px}
.type{font-size:8.5px;color:#666;padding-left:14px}
.stars{color:var(--star);font-size:12px;letter-spacing:1px}
.amount{text-align:center;font-size:9.5px;color:#444;line-height:11px}
.amount em{font-style:normal;color:var(--red)}
.req{font-size:8px;color:#777;line-height:10px;padding-left:8px}
.see{display:flex;gap:4px;padding-left:5px}
.see span{font-size:8px;font-weight:700;color:var(--white);padding:7px 7px;border-radius:2px;background:var(--red)}
.see span.go{background:var(--green);padding:7px 9px}
.row .desc{position:absolute;left:102px;top:60px;font-size:8.5px;color:#444}

/* articles */
.articles{left:645px;top:411px;width:186px;height:327px}
.articles article{padding:8px 12px 6px;border-bottom:1px solid #e6e6e6}
.articles h5{font-size:10px;color:#333;font-weight:500;margin-bottom:2px}
.articles h5.hot{color:var(--red)}
.articles p{font-size:8px;color:#777;line-height:10px}
.articles time{display:flex;align-items:center;gap:4px;font-size:7.5px;color:#999;margin-top:3px}
.articles time i{width:7px;height:7px;border:1px solid #aaa}

/* calculator */
.calc{left:645px;top:745px;width:186px;height:208px}
.calc form{padding:10px 13px}
.calc label{display:block;font-size:8.5px;color:#444;margin-bottom:3px}
.field{height:19px;background:#efefef;border:1px solid #ddd;font-size:8.5px;color:#555;padding:4px 6px;margin-bottom:7px}
.calc .split{display:flex;gap:12px}
.calc .split>div{flex:1}
.calc .split>div+div{flex:.7}
.calc .btn{display:inline-block;font-size:9.5px;padding:4px 12px}

/* footer */
.footer{left:126px;top:988px;width:705px;height:160px;background:linear-gradient(#2a2a2a,#363636);color:#bbb}
.footer h3{font-size:11px;color:var(--white);font-weight:400;display:flex;align-items:center;gap:6px}
.about{position:absolute;left:19px;top:18px;width:216px}
.about p{font-size:8px;line-height:10.5px;margin:9px 0 6px;color:#aaa}
.about .btn{display:inline-block;font-size:8px;padding:2px 10px}
.sitemap{position:absolute;left:298px;top:18px;width:220px}
.sitemap ul{columns:2;margin-top:8px}
.sitemap li{font-size:8px;line-height:13.5px;padding-left:11px;position:relative;color:#bbb}
.sitemap li::before{content:"";position:absolute;left:1px;top:4px;width:4px;height:4px;border:1px solid #999;border-radius:50%}
.sitemap li.active{background:var(--red);color:#fff;width:88px}
.mapbox{position:absolute;left:534px;top:33px;width:149px;height:54px;background:linear-gradient(135deg,#e8e6e0,#cfcbc2)}
.footer-contact{position:absolute;left:534px;top:102px;display:flex;gap:8px;align-items:center}
.footer-contact small{display:block;font-size:8.5px;color:#ddd}
.footer-contact strong{color:var(--red);font-size:14px;font-weight:700}

.copyright{left:143px;top:1169px;font-size:8.5px;color:#666}
.foot-brand{left:718px;top:1164px;font-size:13px;color:#333;font-weight:500}
</style>
</head>
<body>

<header>
  <div class="abs brand">pellrowatt.example</div>
  <div class="abs hotline">
    <span class="phone-badge"><svg width="11" height="11" viewBox="0 0 24 24"><path fill="#333" d="M6.6 10.8a15 15 0 006.6 6.6l2.2-2.2c.3-.3.7-.4 1-.2 1.1.4 2.3.6 3.6.6.6 0 1 .4 1 1V20c0 .6-.4 1-1 1A17 17 0 013 4c0-.6.4-1 1-1h3.5c.6 0 1 .4 1 1 0 1.3.2 2.5.6 3.6.1.3 0 .7-.2 1z"/></svg></span>
    <div><small>Contact Now</small><strong>1800 0000 472</strong></div>
  </div>
  <div class="abs search">Search <svg width="9" height="9" viewBox="0 0 10 10"><circle cx="4" cy="4" r="3" fill="none" stroke="#aaa" stroke-width="1.3"/><path d="M6.3 6.3L9 9" stroke="#aaa" stroke-width="1.3"/></svg></div>
</header>

<nav class="abs mainnav">
  <a>Home</a><a>All About Finances</a><a class="active">Finance Dictionary</a><a>Safety</a><a>About Us</a><a>Plug</a><a>Forum</a><a>Contact Us</a>
</nav>
<div class="abs subnav">
  <span>All loans</span><span>Small loans</span><span>Large loans</span><span>Consumer</span><span>Credit</span><span>Favorite Track</span><span>News</span>
  <span class="connect">Connect With Us <i class="dot"></i><i class="dot"></i><i class="dot"></i><i class="dot"></i><i class="dot"></i></span>
</div>

<div class="abs hero" role="img" aria-label="Photo of two business people working together at a laptop in a bright office">
  <div class="dots"><i></i><i></i><i></i><i></i></div>
</div>

<aside class="abs panel chooser">
  <div class="panel-head"><svg width="11" height="11" viewBox="0 0 12 12"><path d="M1 6l3.5 3.5L11 2" stroke="#fff" stroke-width="2" fill="none"/></svg>Choose Your Loan Here</div>
  <section><h4>Choose Loan</h4><ul><li>Favoritlån</li><li>Consumer Lending</li><li>Car Loans</li><li>Unsecured Loans</li><li>Consumer loans</li></ul></section>
  <section><h4>Information</h4><ul><li>User Panel</li><li>Calculate a loan</li></ul></section>
  <section style="border:0"><h4>Reconciliation</h4><p>Did you do a private budget?:</p>
    <div class="vote"><span><i></i>Yes</span><span><i style="background:#666"></i>No</span><span class="btn">Vote</span></div></section>
</aside>

<main class="abs panel lending">
  <div class="panel-head"><svg width="11" height="11" viewBox="0 0 12 12"><circle cx="6" cy="3.5" r="2.5" fill="#fff"/><path d="M1 12c0-3 2-5 5-5s5 2 5 5z" fill="#fff"/></svg>Consumer Lending</div>
  <div class="cols thead"><div>Supplier</div><div>Type</div><div>Amount</div><div>Requirements</div><div>See</div></div>

  <div class="row"><div class="cols"><div class="supplier"><div class="logo-box"><b></b>Lunvik</div></div><div class="type">Consumer Loans<div class="stars">★★★★★</div></div><div class="amount">20,000<br><em>to</em><br>350,000</div><div class="req">Anual income less than 20,000 $. Age of 20. No betalningsanm.</div><div class="see"><span>Read more</span><span class="go">Apply Now</span></div></div><div class="supplier-name">Lunvik</div><div class="desc">Lunvik Vidlånet - Årets lån (Ekonomibladet)</div></div>

  <div class="row"><div class="cols"><div class="supplier"><div class="logo-box">Korvala</div></div><div class="type">Consumer Loans<div class="stars">★★★★★</div></div><div class="amount">20,000<br><em>to</em><br>350,000</div><div class="req">Anual income less than 20,000 $. Age of 20. No betalningsanm.</div><div class="see"><span>Read more</span><span class="go">Apply Now</span></div></div><div class="supplier-name">Korvala Bank</div><div class="desc">Spara både tid och pengar genom att skriva under ditt låneavtal elektroniskt!</div></div>

  <div class="row"><div class="cols"><div class="supplier"><div class="logo-box">Pennydrift</div></div><div class="type">Consumer Loans<div class="stars">★★★★★</div></div><div class="amount">20,000<br><em>to</em><br>350,000</div><div class="req">Anual income less than 20,000 $. Age of 20. No betalningsanm.</div><div class="see"><span>Read more</span><span class="go">Apply Now</span></div></div><div class="supplier-name">Pennydrift</div><div class="desc">Pennydrift the loan broker online that offer quick and easy loan of up to £ 15,000</div></div>

  <div class="row"><div class="cols"><div class="supplier"><div class="logo-box"><b></b>Selvira</div></div><div class="type">Consumer Loans<div class="stars">★★★★★</div></div><div class="amount">20,000<br><em>to</em><br>350,000</div><div class="req">Anual income less than 20,000 $. Age of 20. No betalningsanm.</div><div class="see"><span>Read more</span><span class="go">Apply Now</span></div></div><div class="supplier-name">Selvira Finans</div><div class="desc">Lunvik Vidlånet - Årets lån (Ekonomibladet)</div></div>

  <div class="row"><div class="cols"><div class="supplier"><div class="logo-box">Brackwell</div></div><div class="type">Consumer Loans<div class="stars">★★★★★</div></div><div class="amount">20,000<br><em>to</em><br>350,000</div><div class="req">Anual income less than 20,000 $. Age of 20. No betalningsanm.</div><div class="see"><span>Read more</span><span class="go">Apply Now</span></div></div><div class="supplier-name">Brackwell</div><div class="desc">Spara både tid och pengar genom att skriva under ditt låneavtal elektroniskt!</div></div>

  <div class="row" style="border:0"><div class="cols"><div class="supplier"><div class="logo-box">Merrowdale</div></div><div class="type">Consumer Loans<div class="stars">★★★★★</div></div><div class="amount">20,000<br><em>to</em><br>350,000</div><div class="req">Anual income less than 20,000 $. Age of 20. No betalningsanm.</div><div class="see"><span>Read more</span><span class="go">Apply Now</span></div></div><div class="supplier-name">Merrowdale Bank</div><div class="desc">Pennydrift the loan broker online that offer quick and easy loan of up to £ 15,000</div></div>
</main>

<aside class="abs panel articles">
  <div class="panel-head"><svg width="12" height="10" viewBox="0 0 12 10"><rect x=".5" y=".5" width="11" height="9" fill="none" stroke="#fff"/><path d="M2 3h8M2 5h8M2 7h5" stroke="#fff"/></svg>Latest Articles</div>
  <article><h5>Need for economic guidance?</h5><p>Even for the best may be the economy led by the track, spending and assume debts getting bigger and bigger.</p><time><i></i>6 December 2012</time></article>
  <article><h5 class="hot">Earn money to publish an e-book</h5><p>Many people have a dream to be able to supplement their full time job with an extra source of income that can brighten up your</p><time><i></i>6 December 2012</time></article>
  <article><h5>Osterly Bank Subsidiary Quellmark ...</h5><p>By Tamsin HollowayThe recent high profile acquisition of UK based mobile technolo...</p><time><i></i>6 December 2012</time></article>
  <article style="border:0"><h5>Save money in the private budget</h5><p>By examining the market and with a modicum of kindness in everyday life, there may be a lot of money to save in private</p><time><i></i>6 December 2012</time></article>
</aside>

<aside class="abs panel calc">
  <div class="panel-head"><svg width="10" height="12" viewBox="0 0 10 12"><rect x=".5" y=".5" width="9" height="11" fill="none" stroke="#fff"/><rect x="2" y="2" width="6" height="2.5" fill="#fff"/></svg>Calculate a Loan</div>
  <form>
    <label>Loan Amount:</label><div class="field">25,000</div>
    <div class="split"><div><label>Effective interest rate:</label><div class="field">15</div></div><div><label>Maturity:</label><div class="field">10</div></div></div>
    <label>Monthly cost: GBP</label><div class="field">403.34</div>
    <span class="btn">Calculate</span>
  </form>
</aside>

<footer class="abs footer">
  <div class="about">
    <h3><svg width="8" height="12" viewBox="0 0 8 12"><circle cx="4" cy="2" r="1.5" fill="#fff"/><rect x="2.5" y="4.5" width="3" height="7" fill="#fff"/></svg>About Company</h3>
    <p>Lorem Ipsum is simply dummy text of the printing and typesetting industry. Lorem Ipsum has been the industry's standard dummy text ever since the 1500s, when an unknown printer took a galley of type and scrambled it to make a type specimen book. It has survived not only five centuries, but also the leap into electronic typesetting, remaining essentially unchanged.</p>
    <span class="btn">Learn more</span>
  </div>
  <div class="sitemap">
    <h3><svg width="11" height="10" viewBox="0 0 11 10"><path d="M5.5 0L11 5H9v5H2V5H0z" fill="#fff"/></svg>Site Map</h3>
    <ul><li>Home</li><li class="active">All About Finances</li><li>Finance Dictionary</li><li>Safety</li><li>Information</li><li>Calculate Loan</li><li>About Us</li><li>Consumer Lending</li><li>Plug</li><li>Forum</li><li>Articls</li><li>Contact Us</li></ul>
  </div>
  <div class="mapbox" role="img" aria-label="Small street map showing the office location with a red pin"></div>
  <div class="footer-contact">
    <span class="phone-badge"><svg width="11" height="11" viewBox="0 0 24 24"><path fill="#fff" d="M6.6 10.8a15 15 0 006.6 6.6l2.2-2.2c.3-.3.7-.4 1-.2 1.1.4 2.3.6 3.6.6.6 0 1 .4 1 1V20c0 .6-.4 1-1 1A17 17 0 013 4c0-.6.4-1 1-1h3.5c.6 0 1 .4 1 1 0 1.3.2 2.5.6 3.6.1.3 0 .7-.2 1z"/></svg></span>
    <div><small>Contact Now</small><strong>1800 0000 472</strong></div>
  </div>
</footer>

<div class="abs copyright">Copyrights © 2012 pellrowatt.example</div>
<div class="abs foot-brand">pellrowatt.example</div>

</body>
</html>
```